Therapist website

I need a sqaure space web design for my therapy practice. I need a home page, a services page with 4 subpages, an about me, an insurnace page, a contact page, an EMDR page

```html
<!DOCTYPE html>
<html lang="en">
<head>
<meta charset="utf-8">
<title>Oak Meadow Counseling</title>
<link href="https://fonts.googleapis.com/css2?family=Oswald:wght@300;400&family=Open+Sans:wght@400;600&display=swap" rel="stylesheet">
<style>
:root{
  --teal:#2a8f96;
  --teal-dark:#1f7b82;
  --ink:#333;
  --muted:#666;
  --line:#e6e6e6;
  --footer:#262626;
  --white:#fff;
}
*{box-sizing:border-box;margin:0;padding:0}
html,body{width:1200px;height:4627px;overflow:hidden}
body{position:relative;background:var(--white);font-family:"Open Sans",Arial,sans-serif;color:var(--ink)}
.abs{position:absolute}
.heading{font-family:"Oswald","Arial Narrow",sans-serif;font-weight:300;text-transform:uppercase;color:#444}
.copy{font-size:11px;line-height:24px;color:var(--muted)}
.copy.dense{line-height:22px}
.btn{position:absolute;height:40px;border:2px solid var(--teal);border-radius:20px;color:var(--teal);font-family:"Oswald",sans-serif;font-size:14px;text-transform:uppercase;display:flex;align-items:center;justify-content:center;background:var(--white)}
.btn.solid{background:var(--teal);color:var(--white)}
.btn.ghost{background:transparent;border-color:var(--white);color:var(--white)}
.photo{position:absolute}

.topline{left:0;top:0;width:1200px;height:5px;background:var(--teal)}
.nav{top:82px;font-family:"Oswald",sans-serif;font-size:15px;text-transform:uppercase;color:#333}
.nav.active{color:var(--teal)}
.brand{font-family:"Oswald",sans-serif;font-weight:400;color:var(--teal);text-transform:uppercase;display:flex;align-items:center;gap:10px}
.brand .dot{width:16px;height:16px;border-radius:50%;background:var(--teal)}

.hero{left:0;top:136px;width:1200px;height:567px;background:linear-gradient(160deg,#8fae7a 0%,#c9a27f 40%,#a46a4e 65%,#6f8b5e 100%)}
.hero-title{left:0;top:510px;width:1200px;text-align:center;color:var(--white);font-size:44px}
.hero-sub{left:0;top:575px;width:1200px;text-align:center;color:rgba(255,255,255,.9);font-size:36px}

.title-row{left:0;width:1200px;display:flex;align-items:center;justify-content:center;gap:18px}
.title-row .rule{width:70px;height:2px;background:var(--teal)}
.title-row .heading{font-size:44px}

.card-title{font-family:"Oswald",sans-serif;font-size:17px;text-transform:uppercase;color:#333}

.band-text{color:var(--white)}
.footer{left:0;top:4338px;width:1200px;height:289px;background:var(--footer)}
.fnav{left:0;top:4508px;width:1200px;display:flex;justify-content:center;gap:28px;font-family:"Oswald",sans-serif;font-size:15px;color:var(--white);text-transform:uppercase}
.fnav span.sep{color:#888}
</style>
</head>
<body>

<header>
  <div class="abs topline"></div>
  <div class="abs nav active" style="left:163px">Home</div>
  <div class="abs nav" style="left:268px">Services</div>
  <div class="abs nav" style="left:393px">About</div>
  <div class="abs nav" style="left:745px">Insurance</div>
  <div class="abs nav" style="left:880px">EMDR</div>
  <div class="abs nav" style="left:984px">Contact</div>
  <div class="abs brand" style="left:490px;top:62px;width:220px;justify-content:center;font-size:28px"><span class="dot"></span>Oak Meadow</div>
  <div class="abs" style="left:490px;top:104px;width:220px;text-align:center;font-family:'Oswald',sans-serif;font-size:10px;letter-spacing:3px;color:var(--teal);text-transform:uppercase">Family Counseling</div>
</header>

<section>
  <div class="abs hero" role="img" aria-label="Smiling family of four outdoors in sunlight"></div>
  <div class="abs" style="left:330px;top:500px;width:540px;height:70px;background:rgba(0,0,0,.15)"></div>
  <div class="abs heading hero-title">Oak Meadow Counseling</div>
  <div class="abs heading hero-sub">Sed ut perspiciatis unde omnis iste natus error sit</div>
</section>

<section>
  <div class="abs" style="left:562px;top:665px;width:76px;height:76px;border-radius:50%;background:var(--white)"></div>
  <div class="abs" style="left:584px;top:687px;width:32px;height:32px;border-radius:50%;background:var(--teal)"></div>
  <div class="abs title-row" style="top:730px"><span class="rule"></span><span class="heading">Our Services</span><span class="rule"></span></div>

  <div class="photo" style="left:86px;top:820px;width:327px;height:207px;background:linear-gradient(135deg,#7a9a5a,#c8b48a,#4f6a3a)" role="img" aria-label="Family portrait in autumn park"></div>
  <div class="photo" style="left:436px;top:820px;width:327px;height:207px;background:linear-gradient(135deg,#8a6a3a,#c79a5e,#5a4a2a)" role="img" aria-label="Adult hand holding a child's hand"></div>
  <div class="photo" style="left:786px;top:820px;width:327px;height:207px;background:linear-gradient(135deg,#d9c7a8,#c99a6a,#e8dcc6)" role="img" aria-label="Mother hugging young daughter"></div>

  <div class="abs card-title" style="left:86px;top:1043px">Family &amp; Marital Therapy</div>
  <div class="abs card-title" style="left:436px;top:1043px">Attachment / Adoption Therapy</div>
  <div class="abs card-title" style="left:786px;top:1043px">Pre-Adoption Training</div>

  <p class="abs copy" style="left:86px;top:1082px;width:327px">Sed ut perspiciatis unde omnis iste natus error sit voluptatem accusantium doloremque laudantium, totam rem aperiam ea architecto beatae vitae dicta sunt explicabo.</p>
  <p class="abs copy" style="left:436px;top:1082px;width:327px">Sed ut perspiciatis unde omnis iste natus error sit voluptatem accusantium doloremque laudantium, totam rem aperiam ea architecto beatae vitae dicta sunt explicabo.</p>
  <p class="abs copy" style="left:786px;top:1082px;width:327px">Sed ut perspiciatis unde omnis iste natus error sit voluptatem accusantium doloremque laudantium, totam rem aperiam ea architecto beatae vitae dicta sunt explicabo.</p>

  <div class="btn" style="left:86px;top:1180px;width:130px">Read More</div>
  <div class="btn" style="left:436px;top:1180px;width:130px">Read More</div>
  <div class="btn" style="left:786px;top:1180px;width:130px">Read More</div>
</section>

<section>
  <div class="photo" style="left:0;top:1280px;width:1200px;height:386px;background:linear-gradient(90deg,#7f9aa8 0%,#b7c6cc 45%,#e4ecef 70%,#f2f6f7 100%)" role="img" aria-label="Mother and daughter leaning on a wooden fence"></div>
  <div class="abs heading" style="left:700px;top:1322px;font-size:44px">About Me</div>
  <p class="abs copy" style="left:700px;top:1385px;width:420px;color:#444">Welcome to Oak Meadow Family Counseling and thank you for visiting my website to learn more about whether I may be a good fit for your current life struggle. I value bringing my clients hope, encouragement and support and working together to find the answers that bring.</p>
  <div class="btn" style="left:700px;top:1527px;width:130px;background:transparent;border-color:#555;color:#444">Read More</div>
</section>

<section>
  <div class="abs heading" style="left:86px;top:1760px;font-size:44px">Approach</div>
  <p class="abs copy dense" style="left:86px;top:1838px;width:500px">I believe that many struggles are rooted in relationships and therefore practice from modalities and models that are based in relationship such as family systems and psychodynamic. However, within the use of these modalities I am focused on helping clients find solutions and answers, not just insight. My goal is to help you find relief from your struggles. I am trained in EMDR and use it often, unless the client does not desire to or the use is contraindicated. For more information on EMDR you can read more here.</p>
  <div class="btn" style="left:86px;top:2024px;width:130px">Read More</div>
  <div class="photo" style="left:611px;top:1740px;width:500px;height:318px;background:linear-gradient(180deg,#4a7fc4 0%,#a9c8ea 40%,#d9b56a 60%,#b88a3e 100%)" role="img" aria-label="Two people walking through a wheat field under blue sky"></div>
</section>

<section>
  <div class="photo" style="left:0;top:2129px;width:1200px;height:391px;background:linear-gradient(180deg,#bcd9dd 0%,#dfeadf 50%,#c9a765 80%,#a98647 100%)" role="img" aria-label="Girl with arms raised in a golden wheat field"></div>
  <div class="abs heading" style="left:620px;top:2210px;font-size:44px;color:#3a3a3a">General EMDR Information</div>
  <p class="abs copy" style="left:620px;top:2272px;width:470px;color:#333">EMDR (Eye Movement Desensitization and Reprocessing) is a psychotherapy treatment developed by Dr. Helen Marsh that enables people to heal from the symptoms and emotional distress that are the result of disturbing life experiences and is based on the adaptive information processing model (AIP).</p>
  <div class="btn solid" style="left:620px;top:2410px;width:130px">Read More</div>
</section>

<section>
  <div class="abs heading" style="left:86px;top:2614px;font-size:44px">Insurance</div>
  <p class="abs copy dense" style="left:86px;top:2692px;width:500px">I believe that many struggles are rooted in relationships and therefore practice from modalities and models that are based in relationship such as family systems and psychodynamic. However, within the use of these modalities I am focused on helping clients find solutions and answers, not just insight. My goal is to help you find relief from your struggles. I am trained in EMDR and use it often, unless the client does not desire to or the use is contraindicated. For more information on EMDR you can read more here.</p>
  <div class="btn" style="left:86px;top:2880px;width:130px">Read More</div>
  <div class="photo" style="left:611px;top:2591px;width:500px;height:318px;background:linear-gradient(135deg,#4e6a2e,#9aa85a,#3d4f22)" role="img" aria-label="Father and son smiling among autumn leaves"></div>
</section>

<section>
  <div class="photo" style="left:0;top:2977px;width:1200px;height:401px;background:linear-gradient(90deg,#237f86,#2f949b 50%,#237f86)" role="img" aria-label="Teal tinted family photo background"></div>
  <div class="abs title-row" style="top:3064px"><span class="rule" style="background:var(--white)"></span><span class="heading" style="color:var(--white)">Oak Meadow Counseling</span><span class="rule" style="background:var(--white)"></span></div>
  <p class="abs copy band-text" style="left:220px;top:3142px;width:760px;text-align:center">I have worked in residential treatment and in community mental health centers prior to starting a private practice. I consider myself a life long learner and crave learning new information. I have participated in extensive post graduate training related to issues of adoption, attachment, early developmental trauma, relationship struggles, depression, anxiety, and parenting.</p>
  <div class="btn ghost" style="left:535px;top:3260px;width:130px">Read More</div>
</section>

<section>
  <div class="abs title-row" style="top:3422px"><span class="rule"></span><span class="heading">Our Subscribe</span><span class="rule"></span></div>
  <p class="abs copy" style="left:0;top:3494px;width:1200px;text-align:center">Sed ut perspiciatis unde omnis iste natus error sit voluptatem accusantium doloremque laudantium, totam rem aperiam</p>
  <div class="abs" style="left:238px;top:3557px;width:576px;height:49px;border:1px solid var(--line);font-size:11px;color:#777;padding:16px 18px">Enter Your Email Id</div>
  <div class="abs" style="left:814px;top:3557px;width:149px;height:49px;background:var(--teal);color:var(--white);font-family:'Oswald',sans-serif;font-size:16px;text-transform:uppercase;display:flex;align-items:center;justify-content:center">Subscribe</div>
</section>

<section>
  <div class="photo" style="left:86px;top:3665px;width:509px;height:300px;background:linear-gradient(180deg,#c9a45a,#e0c27c,#a8843e)" role="img" aria-label="Boy standing in a wheat field"></div>
  <div class="photo" style="left:605px;top:3665px;width:253px;height:300px;background:linear-gradient(135deg,#6b7a3a,#b69a5a)" role="img" aria-label="Father and son in autumn"></div>
  <div class="photo" style="left:867px;top:3665px;width:247px;height:300px;background:linear-gradient(135deg,#b07a3a,#e0b07a)" role="img" aria-label="Hands holding"></div>
  <div class="photo" style="left:86px;top:3977px;width:250px;height:299px;background:linear-gradient(135deg,#dcc8a8,#c09070)" role="img" aria-label="Mother hugging daughter"></div>
  <div class="photo" style="left:346px;top:3977px;width:249px;height:299px;background:linear-gradient(135deg,#7a8a4a,#c7a86a)" role="img" aria-label="Family portrait outdoors"></div>
  <div class="photo" style="left:605px;top:3977px;width:509px;height:299px;background:linear-gradient(180deg,#cfe0e2,#e5dcc0 55%,#b8944e)" role="img" aria-label="Girl in a wheat field"></div>
</section>

<footer>
  <div class="abs footer"></div>
  <div class="abs brand" style="left:490px;top:4410px;width:220px;justify-content:center;font-size:28px"><span class="dot"></span>Oak Meadow</div>
  <div class="abs" style="left:490px;top:4452px;width:220px;text-align:center;font-family:'Oswald',sans-serif;font-size:10px;letter-spacing:3px;color:var(--teal);text-transform:uppercase">Family Counseling</div>
  <div class="abs" style="left:420px;top:4480px;width:360px;height:1px;background:#444"></div>
  <nav class="abs fnav"><span>Home</span><span class="sep">|</span><span>Services</span><span class="sep">|</span><span>About</span><span class="sep">|</span><span>Insurance</span><span class="sep">|</span><span>EMDR</span><span class="sep">|</span><span>Contact</span></nav>
  <div class="abs" style="left:0;top:4556px;width:1200px;text-align:center;font-size:11px;color:#ccc">© Copyright 2016 Oak Meadow Counseling All Rights Reserved</div>
</footer>

</body>
</html>
```